diamondscoutline.com - Social Media Branding

diamondscoutline.com --> Social Media Re-Branding & Graphics
Facebook: @dmndscoutline - Instagram: @diamondscoutline - Twitter: @dmndscoutline

Looking to find a good designer to help with my diamondscoutline.com social media sites!
- facebook banner
- twitter banner
- instagram template (square and banner size)
- Quote or Information Template
- Committed Template (uniformed) - see the ones I made (& i am no professional) at diamondscoutline.com/committed - needs to have diamondscoutline.com logo, room for: the committed school and the team the player plays on.

Also willing to pay extra for a graphic that is the "complete package" that detail all of the steps of the recruiting process detailed in diamondscoutline.com

Font styles to use
Sans Serif

Colors
ec1f27
fbee3e

```html
<!DOCTYPE html>
<html lang="en">
<head>
<meta charset="utf-8">
<title>Our Complete Package – diamondscoutline.com</title>
<link rel="stylesheet" href="https://fonts.googleapis.com/css2?family=Jost:wght@400;600;700;800&display=swap">
<style>
  :root {
    --backdrop: #545454;
    --paper: #ffffff;
    --brand-red: #bd1e2f;
    --ink: #231f20;
    --body-ink: #2b2b2b;
    --gold: #f7e463;
    --lime: #dddc00;
    --green: #227a0e;
    --teal: #00c896;
    --orange: #f7901e;
    --blue: #0067a8;
    --sky: #cfe4f2;
    --foliage: #6d8a4e;
  }
  * { box-sizing: border-box; margin: 0; padding: 0; }
  html, body { width: 1200px; height: 688px; overflow: hidden; }
  body {
    background: var(--backdrop);
    font-family: "Jost", "Century Gothic", sans-serif;
    position: relative;
  }
  .board {
    position: absolute;
    top: 46px;
    width: 534px;
    height: 598px;
    background: var(--paper);
    overflow: hidden;
    box-shadow: 0 2px 8px rgba(0,0,0,.25);
  }
  .board--warm { left: 46px; }
  .board--spectrum { left: 618px; }

  .board__title {
    position: absolute;
    top: 48px;
    left: 0;
    width: 100%;
    padding-left: 86px;
    font-size: 30px;
    font-weight: 800;
    letter-spacing: .3px;
    color: var(--ink);
    white-space: nowrap;
  }
  .board__title .accent { color: var(--brand-red); }

  .path-art {
    position: absolute;
    inset: 0;
    width: 534px;
    height: 598px;
  }
  .step-number {
    font-family: "Jost", sans-serif;
    font-weight: 700;
    font-size: 52px;
    fill: #ffffff;
    text-anchor: middle;
    dominant-baseline: central;
  }

  .step {
    position: absolute;
    width: 180px;
  }
  .step__heading {
    font-size: 12.5px;
    font-weight: 700;
    line-height: 12.5px;
    color: var(--brand-red);
    letter-spacing: .3px;
    margin-bottom: 3px;
  }
  .step__text {
    font-size: 9.4px;
    line-height: 11px;
    color: var(--body-ink);
    letter-spacing: .15px;
  }
  .step--starter  { left: 327px; top: 137px; }
  .step--monthly  { left: 35px;  top: 172px; width: 160px; }
  .step--prepare  { left: 327px; top: 224px; width: 190px; }
  .step--calls    { left: 34px;  top: 279px; width: 160px; }
  .step--commit   { left: 330px; top: 333px; }
  .step--done     { left: 35px;  top: 386px; }

  .field-photo {
    position: absolute;
    left: 0;
    bottom: 0;
    width: 100%;
    height: 156px;
    background: linear-gradient(180deg, rgba(255,255,255,1) 0%, var(--sky) 30%, #a9c3cf 50%, var(--foliage) 85%, #55703c 100%);
  }
  .brand-mark {
    position: absolute;
    left: 146px;
    top: 520px;
    display: flex;
    align-items: center;
    gap: 8px;
    color: #ffffff;
    font-size: 17px;
    font-weight: 700;
  }
  .brand-mark__dot {
    width: 22px;
    height: 22px;
    border-radius: 50%;
    background: #ffffff;
    opacity: .9;
  }
</style>
</head>
<body>

<!-- Warm gradient edition -->
<section class="board board--warm">
  <h1 class="board__title"><span class="accent">OUR</span> COMPLETE PACKAGE</h1>

  <svg class="path-art" viewBox="0 0 1113 1245" aria-hidden="true">
    <defs>
      <linearGradient id="warmBadge" x1="0" y1="0" x2="1" y2="0">
        <stop offset="0" stop-color="#bd1e2f"/>
        <stop offset="1" stop-color="#f7e463"/>
      </linearGradient>
    </defs>
    <path fill="none" stroke="var(--brand-red)" stroke-width="22"
      d="M237 257 L584 257
         A71 71 0 1 1 534 378
         A71 71 0 1 0 534 476
         A71 71 0 1 1 531 575
         A71 71 0 1 0 534 677
         A71 71 0 1 1 530 778
         A71 71 0 1 0 485 903
         L832 903"/>
    <g fill="url(#warmBadge)">
      <circle cx="584" cy="328" r="45"/>
      <circle cx="484" cy="426" r="45"/>
      <circle cx="581" cy="525" r="45"/>
      <circle cx="484" cy="627" r="45"/>
      <circle cx="580" cy="728" r="45"/>
      <circle cx="485" cy="832" r="45"/>
    </g>
    <text class="step-number" x="584" y="330">1</text>
    <text class="step-number" x="484" y="428">2</text>
    <text class="step-number" x="581" y="527">3</text>
    <text class="step-number" x="484" y="629">4</text>
    <text class="step-number" x="580" y="730">5</text>
    <text class="step-number" x="485" y="834">6</text>
  </svg>

  <div class="step step--starter">
    <h2 class="step__heading">STARTER PACK:</h2>
    <p class="step__text">Step-by-Step on how to start the<br>Recruiting Process</p>
  </div>
  <div class="step step--monthly">
    <h2 class="step__heading">MONTHLY LESSON:</h2>
    <p class="step__text">Breakdown of what you should be doing (email, video, social media &amp; MORE) every month to build relationships with college coaches</p>
  </div>
  <div class="step step--prepare">
    <h2 class="step__heading">PREPARING FOR SEPTEMBER<br>1ST (JUNIOR YEAR)</h2>
    <p class="step__text">How to Prepare for Calls &amp; What to<br>Say to College Coaches</p>
  </div>
  <div class="step step--calls">
    <h2 class="step__heading">TURNING PHONE CALLS<br>INTO OFFERS</h2>
    <p class="step__text">Talking with Schools? - How to get<br>the Offer</p>
  </div>
  <div class="step step--commit">
    <h2 class="step__heading">HOW TO COMMIT:</h2>
    <p class="step__text">What Questions to Ask &amp; What to<br>get in Writing</p>
  </div>
  <div class="step step--done">
    <h2 class="step__heading">COMMITTED:</h2>
    <p class="step__text">Learn Everything you Need to Do<br>After you Say "YES!"</p>
  </div>

  <div class="field-photo" role="img" aria-label="Photo of a softball batter in a helmet at the plate, trees and sky behind"></div>
  <div class="brand-mark"><span class="brand-mark__dot"></span>diamondscoutline.com</div>
</section>

<!-- Multicolour edition -->
<section class="board board--spectrum">
  <h1 class="board__title"><span class="accent">OUR</span> COMPLETE PACKAGE</h1>

  <svg class="path-art" viewBox="0 0 1113 1245" aria-hidden="true">
    <g fill="none" stroke-width="22">
      <path stroke="var(--lime)" d="M237 257 L584 257 A71 71 0 1 1 534 378"/>
      <path stroke="var(--green)" d="M534 378 A71 71 0 1 0 534 476"/>
      <path stroke="var(--teal)" d="M534 476 A71 71 0 1 1 531 575"/>
      <path stroke="var(--orange)" d="M531 575 A71 71 0 1 0 534 677"/>
      <path stroke="var(--blue)" d="M534 677 A71 71 0 1 1 530 778"/>
      <path stroke="var(--brand-red)" d="M530 778 A71 71 0 1 0 485 903 L832 903"/>
    </g>
    <circle cx="584" cy="328" r="45" fill="var(--lime)"/>
    <circle cx="484" cy="426" r="45" fill="var(--green)"/>
    <circle cx="581" cy="525" r="45" fill="var(--teal)"/>
    <circle cx="484" cy="627" r="45" fill="var(--orange)"/>
    <circle cx="580" cy="728" r="45" fill="var(--blue)"/>
    <circle cx="485" cy="832" r="45" fill="var(--brand-red)"/>
    <text class="step-number" x="584" y="330">1</text>
    <text class="step-number" x="484" y="428">2</text>
    <text class="step-number" x="581" y="527">3</text>
    <text class="step-number" x="484" y="629">4</text>
    <text class="step-number" x="580" y="730">5</text>
    <text class="step-number" x="485" y="834">6</text>
  </svg>

  <div class="step step--starter">
    <h2 class="step__heading">STARTER PACK:</h2>
    <p class="step__text">Step-by-Step on how to start the<br>Recruiting Process</p>
  </div>
  <div class="step step--monthly">
    <h2 class="step__heading">MONTHLY LESSON:</h2>
    <p class="step__text">Breakdown of what you should be doing (email, video, social media &amp; MORE) every month to build relationships with college coaches</p>
  </div>
  <div class="step step--prepare">
    <h2 class="step__heading">PREPARING FOR SEPTEMBER<br>1ST (JUNIOR YEAR)</h2>
    <p class="step__text">How to Prepare for Calls &amp; What to<br>Say to College Coaches</p>
  </div>
  <div class="step step--calls">
    <h2 class="step__heading">TURNING PHONE CALLS<br>INTO OFFERS</h2>
    <p class="step__text">Talking with Schools? - How to get<br>the Offer</p>
  </div>
  <div class="step step--commit">
    <h2 class="step__heading">HOW TO COMMIT:</h2>
    <p class="step__text">What Questions to Ask &amp; What to<br>get in Writing</p>
  </div>
  <div class="step step--done">
    <h2 class="step__heading">COMMITTED:</h2>
    <p class="step__text">Learn Everything you Need to Do<br>After you Say "YES!"</p>
  </div>

  <div class="field-photo" role="img" aria-label="Photo of a softball batter in a helmet at the plate, trees and sky behind"></div>
  <div class="brand-mark"><span class="brand-mark__dot"></span>diamondscoutline.com</div>
</section>

</body>
</html>
```